Office brochure for chronic pain doctor

I need an brochure for my office, and since I want to be able to mail the brochure, I think trifold would be the best size. I treat patients with chronic head and neck pain, as well as sleep apnea. I treat all of the following:

1. headaches
2. myofascial pain, which is a fancy way of saying muscle pain
3. neuropathic pain, which is a fancy way of saying nerve pain
4. TMJ, which stands for the temporomandibular joint (jaw joint)
5. obstructive sleep apnea

The colors will be based on my logo on my website, which you can see at www.BrightJPR.net, and you can learn more about what I do at my website. JPR stands for orofacial pain, which is a speciality training within the field of dentistry but I do not treat teeth. I have high resolution graphics for the brochure so I need someone with an artistic eye to design and lay out the brochure.

The logo colors are:
Purple 9e80bb
Pink f6b1d0
Blue 0f4b8f
Updates

I had a request for the logo in a .ai or .pdf format, which I have just uploaded. Please let me know if you have any other requests. Thank you, Dale

Target Market(s)

80% female, 20% male. I am in an upscale area of Los Angeles called Beverly Hills but I will see a patient from any area around Los Angeles or from any area in the world.

Industry/Entity Type

Training

Colors
6b449b
e567a6
0355a3

Requirements
Must have
• I want a small section of the brochure to feature each of the five areas I treat, and I have included an image to place in each of the five sections. A small section should include a short bio of me, which you can condense from www.brightjpr.net/dale. The brochure must appeal to women since 80% of my patients are female but I don't want to completely ignore men. Most of the pain patients are female, and most of the sleep apnea patients are male.

Here are the colors in my logo
Purple 9e80bb
Pink f6b1d0
Blue 0f4b8f
Should not have
• Anything related to teeth or dentistry.
No decorative or script fonts.

```html
<!DOCTYPE html>
<html lang="en">
<head>
<meta charset="utf-8">
<title>BrightJPR Trifold Brochure</title>
<link rel="stylesheet" href="https://fonts.googleapis.com/css2?family=Open+Sans:wght@300;400;600;700&display=swap">
<style>
:root{
  --purple:#9e80bb;
  --purple-deep:#7f62a6;
  --purple-band:#a58fc4;
  --purple-soft:#cbbade;
  --pink:#f4a9cb;
  --pink-light:#f9cfe2;
  --blue:#0f4b8f;
  --ink:#3f3f42;
  --ink-soft:#6a6a6e;
  --grey-text:#a9a9ad;
  --bio-grey:#8c8d90;
  --paper:#ffffff;
  --stage:#3b3b3d;
}
*{margin:0;padding:0;box-sizing:border-box}
html,body{width:793px;height:1200px;overflow:hidden}
body{background:var(--stage);font-family:"Open Sans",Arial,sans-serif;color:var(--ink);position:relative}

.sheet{position:absolute;left:50px;width:693px;background:var(--paper);overflow:hidden}
.sheet--outside{top:45px;height:470px;
  background:linear-gradient(90deg,#fff 0,#fff 222px,#eeeef0 231px,#fbfbfb 240px,#fff 452px,#eeeef0 462px,#fff 472px)}
.sheet--inside{top:590px;height:540px}

.panel{position:absolute;top:0;height:100%}

/* ---------- outside ---------- */
.cover-photo{position:absolute;left:14px;top:14px;width:196px;height:208px;
  background:linear-gradient(160deg,#e9e6dc 0,#cfc7b8 45%,#9a8e80 75%,#6f6a63 100%)}
.brand-mini{position:absolute;left:6px;top:6px;display:flex;align-items:center;gap:4px;
  font-size:8px;font-weight:600;color:var(--purple)}
.brand-mini .dot{width:9px;height:9px;background:var(--pink)}

.intro-title{position:absolute;left:16px;top:240px;line-height:1.02;color:var(--ink-soft)}
.intro-title .light{display:block;font-size:26px;font-weight:300}
.intro-title .bold{display:block;font-size:26px;font-weight:700;color:#4c4c50}
.intro-copy{position:absolute;left:16px;top:302px;width:202px;font-size:7.2px;line-height:1.42;color:var(--grey-text)}

.topic-band{position:absolute;left:0;top:422px;width:462px;height:48px;background:var(--purple-band)}
.topic-band .words{position:absolute;left:14px;top:2px;color:var(--purple-soft);line-height:.92}
.topic-band .big{display:block;font-size:22px;font-weight:400}
.topic-band .small{display:block;font-size:12.5px}
.topic-band .small.indent{padding-left:104px}

.contacts{position:absolute;left:231px;top:252px;width:231px;text-align:center;color:var(--purple)}
.contacts h2{font-size:17px;font-weight:300;color:var(--pink);letter-spacing:.5px;margin-bottom:3px}
.contacts p{font-size:7.2px;line-height:1.4}

.social{position:absolute;left:240px;top:432px;display:flex;gap:3px}
.social span{width:32px;height:30px;background:var(--pink);color:#fff;font-size:7px;font-weight:600;
  display:flex;align-items:center;justify-content:center}

.brand-lockup{position:absolute;left:476px;top:42px;display:flex;align-items:center;gap:10px}
.brand-lockup .square{width:46px;height:46px;background:var(--pink)}
.brand-lockup .name{font-size:30px;font-weight:600;color:var(--purple)}
.tagline{position:absolute;left:476px;top:106px;font-size:11px;color:#333}
.sleep-photo{position:absolute;left:462px;top:160px;width:231px;height:280px;
  background:linear-gradient(170deg,#f3ede6 0,#e8d5c2 35%,#d9b797 60%,#f4efe9 100%)}
.site-url{position:absolute;left:492px;top:452px;font-size:7px;color:var(--ink-soft)}

/* ---------- inside ---------- */
.banner-photo{position:absolute;left:0;top:0;width:560px;height:142px;
  background:linear-gradient(100deg,#6b8aa0 0,#b9c9d3 25%,#d8cbbd 45%,#e6eef2 70%,#9ec0d0 100%)}
.banner-url{position:absolute;left:12px;top:128px;font-size:7px;color:#fff}
.testimonial{position:absolute;left:286px;top:24px;width:150px;padding:5px 6px;background:rgba(255,255,255,.9);
  font-size:5.4px;line-height:1.35;color:var(--ink)}
.testimonial cite{display:block;text-align:right;font-style:italic;margin-top:2px}

.treatments{position:absolute;left:0;top:148px;width:560px;height:392px;background:#fff}
.treatments .rule{position:absolute;left:0;top:0;width:560px;height:8px;background:var(--pink)}
.treatments .edge{position:absolute;left:0;top:0;width:5px;height:392px;background:var(--pink)}
.treatment{position:absolute;top:12px;width:108px}
.treatment .art{height:118px;border:2px solid var(--pink-light)}
.treatment .tab{position:relative;margin-top:12px;height:26px;background:var(--purple);color:#fff;
  font-size:9.5px;text-align:center;line-height:1.1;display:flex;align-items:center;justify-content:center;text-transform:uppercase}
.treatment .tab::before{content:"";position:absolute;left:50%;top:-6px;margin-left:-7px;
  border-left:7px solid transparent;border-right:7px solid transparent;border-bottom:6px solid var(--purple)}
.treatment .copy{padding:6px 4px 0 6px;font-size:7px;line-height:1.3;color:var(--ink)}
.treatment .copy strong{color:var(--purple-deep);font-size:9px;line-height:1.15}
.art--headache{background:linear-gradient(160deg,#fbe9dc,#e8b79a 60%,#b24a3a)}
.art--myofascial{background:linear-gradient(160deg,#f6e7da,#d88f6f 55%,#a5533c)}
.art--nerve{background:linear-gradient(160deg,#fbece1,#e9c1a6 60%,#8a5a45)}
.art--joint{background:linear-gradient(160deg,#f1e6d0,#c98d7c 55%,#8f3c3a)}
.art--airway{background:linear-gradient(160deg,#fbe6db,#e2a48f 55%,#a8463f)}

.base-strip{position:absolute;top:530px;height:10px}

.bio{position:absolute;left:560px;top:0;width:133px;height:540px;background:var(--bio-grey);color:#fff}
.bio .portrait{position:absolute;left:10px;top:14px;width:113px;height:110px;
  background:linear-gradient(170deg,#e9ecef 0,#cfd3d8 50%,#f5f5f5 100%)}
.bio h3{position:absolute;left:10px;top:134px;font-size:10px;font-weight:400}
.bio h3 b{font-weight:700}
.bio .role{position:absolute;left:10px;top:149px;font-size:6px}
.bio .story{position:absolute;left:10px;top:172px;width:114px;font-size:6px;line-height:1.42}
.bio .story p+p{margin-top:8px}
.bio .brand-foot{position:absolute;left:10px;top:500px;display:flex;align-items:center;gap:5px;
  font-size:10px;font-weight:600;color:#fff}
.bio .brand-foot .square{width:14px;height:14px;background:var(--pink)}
</style>
</head>
<body>

<section class="sheet sheet--outside" aria-label="Brochure outside">
  <div class="panel" style="left:0;width:231px">
    <div class="cover-photo" role="img" aria-label="Photo of a woman pressing her hands to her face in pain">
      <div class="brand-mini"><span class="dot"></span>BrightJPR</div>
    </div>
    <h1 class="intro-title"><span class="light">Learn About</span><span class="bold">Orofacial Pain</span></h1>
    <p class="intro-copy">Orofacial pain, known as JPR for short, is the management of chronic head and neck pain using conservative treatment. A group of dentists at the Westbrook University School of Dentistry in the 1990's started to fill a niche treating patients who had undiagnosed chronic pain in the head and neck including headaches such as migraine, and cluster headaches, head and neck muscle pain, various nerve pains from sharp, shooting electrical pain to dull, aching, burning pain, TMJ, and obstructive sleep apnea.</p>
  </div>

  <div class="contacts">
    <h2>CONTACTS</h2>
    <p>Dale Marlowe, DDS, MBA<br>Diplomate American Board of Jaw &amp; Facial Pain<br>4120 Canyon Way, Suite 210<br>Larkfield, CA 95099<br>555.014.2290</p>
  </div>

  <div class="topic-band">
    <div class="words">
      <span class="big">Headache&nbsp; TMJ</span>
      <span class="small">Nerve and Muscle Pain</span>
      <span class="small indent">Sleep Apnea</span>
    </div>
  </div>
  <nav class="social" aria-label="Social links">
    <span>Circle</span><span>Chirp</span><span>Stream</span><span>Blog</span><span>Plus</span><span>Rate</span>
  </nav>

  <div class="brand-lockup"><span class="square"></span><span class="name">BrightJPR</span></div>
  <p class="tagline">Caring for Head Pain and Sleep Apnea</p>
  <div class="sleep-photo" role="img" aria-label="Photo of a woman sleeping peacefully on a white pillow with a partner behind her"></div>
  <p class="site-url">www.brightjpr.net</p>
</section>

<section class="sheet sheet--inside" aria-label="Brochure inside">
  <div class="banner-photo" role="img" aria-label="Photo of a smiling woman relaxing on a sofa in a bright room"></div>
  <p class="banner-url">www.brightjpr.net</p>
  <blockquote class="testimonial">I had jaw pain for 15 years and spent a lot of time and money being treated for TMJ until Dr. Marlowe correctly diagnosed that my pain was coming from muscles, not my joint. I finally found relief through his gentle care.
    <cite>Renata K., Larkfield, California</cite></blockquote>

  <div class="treatments">
    <div class="rule"></div><div class="edge"></div>

    <article class="treatment" style="left:5px">
      <div class="art art--headache" role="img" aria-label="Illustration of a head showing headache pain area"></div>
      <div class="tab">Headaches</div>
      <p class="copy"><strong>A headache is an ache or pain</strong> occurring anywhere in the face, neck or head. Headache pain is experienced through pain-sensitive structures around the head and neck including blood vessels, nerves, muscles and tissues including the eyes, ears and sinuses. Headaches can range across the intensity spectrum from mild, tolerable pain to severe pain that prohibits daily activities. Headaches are one of the most commonly experienced causes of pain.</p>
    </article>

    <article class="treatment" style="left:116px">
      <div class="art art--myofascial" role="img" aria-label="Illustration of head and neck muscles"></div>
      <div class="tab">Myofascial Pain</div>
      <p class="copy"><strong>Chronic myofascial pain (CMP)</strong> is a chronic pain disease characterized by trigger points in the musculature causing pain in distinct areas of the body. Pain symptoms of CMP can be severe and debilitating. While much of the underlying mechanics of myofascial pain is not clearly understood, research suggests that symptoms are derived from the existence of trigger points within muscles, which are activated by injury or repetitive strain to muscles.</p>
    </article>

    <article class="treatment" style="left:227px">
      <div class="art art--nerve" role="img" aria-label="Illustration of facial nerve pain points"></div>
      <div class="tab">Neuropathic<br>Pain</div>
      <p class="copy"><strong>Neuropathic pain disorders</strong> are a set of pain conditions resulting from disorder or injury to the nervous system. The human nervous system is divided into two general parts: the central nervous system, comprising the brain and spinal cord, and the peripheral nervous system, including nerves that go to the limbs, trunk, face and all outlying areas of the body. When nerves of the peripheral system sense pain from mechanical, chemical or thermal sensations.</p>
    </article>

    <article class="treatment" style="left:338px">
      <div class="art art--joint" role="img" aria-label="Illustration of the jaw joint and surrounding muscles"></div>
      <div class="tab">TMJ</div>
      <p class="copy"><strong>Temporomandibular joint disorder, also known as TMJ, TMD, or TMJD,</strong> is a general term covering any disorder causing inflammation of the temporomandibular joint, which connects the skull to the mandible. There are a number of conditions that can cause pain in the jaw joint and the muscles involved in the closing and opening of the jaw. Disorders affecting the joint can affect a person's ability to eat, speak, swallow, chew, and breathe.</p>
    </article>

    <article class="treatment" style="left:449px">
      <div class="art art--airway" role="img" aria-label="Illustration of a blocked airway during sleep"></div>
      <div class="tab">Obstructive<br>Sleep Apnea</div>
      <p class="copy"><strong>Sleep apnea is a common sleeping disorder</strong> marked by shallow breathing, pauses in breath and labored breathing punctuated by gasping or snoring sounds. Pauses of breath can last from several seconds up to minutes and can happen from five to thirty times or more per hour. A pause may be followed by a choking or snorting sound as the sleeper involuntarily gasps for breath.</p>
    </article>
  </div>

  <div class="base-strip" style="left:0;width:227px;background:var(--pink)"></div>
  <div class="base-strip" style="left:227px;width:222px;background:var(--purple)"></div>
  <div class="base-strip" style="left:449px;width:111px;background:var(--blue)"></div>

  <aside class="bio">
    <div class="portrait" role="img" aria-label="Portrait photo of Dr. Dale Marlowe in a white coat"></div>
    <h3>Dr. Dale <b>Marlowe</b></h3>
    <p class="role">Larkfield Facial Pain Doctor</p>
    <div class="story">
      <p>Do you like change, which is a large part of life today? I do, so mine has been an interesting career. I was born in the Midwest, moved to California as a child, and grew up in a quiet valley town, where I spent my childhood. After high school I attended university in the South, which was a fantastic experience, and then came home to begin my practice. Today I focus entirely on head, neck and sleep care.</p>
      <p>Two of my passions, in addition to my family, were cycling and the outdoors. After an injury of my own I learned firsthand what chronic pain means, and it shaped the way I listen to every patient who walks through my door.</p>
    </div>
    <div class="brand-foot"><span class="square"></span>BrightJPR</div>
  </aside>
</section>

</body>
</html>
```